Lanternfield Prose Studio (LPStudio.net)

We need a Wordpress-based site designed for a client who provides writing and editing services for the IT industry. We have a wireframe complete for the homepage, but need all internal pages designed (based on homepage wireframe) and the entire site coded for WP.

Internal pages include: "Our Work" (with samples & testimonials); "Capabilities" (with sections to address "strategy", "coaching", "writing" and "editing"); "About Us"; and a Contact page.

Will provide all copywriting, writing samples, testimonials, and client logos.

We completely realize/acknowledge the subject matter is visually BORING! Anything at all that can be done to make it look visually appealing would be *great*! Stock photography is fine.

Please feel free to ask any questions whatsoever. Thanks for your time!

```html
<!DOCTYPE html>
<html lang="en">
<head>
<meta charset="utf-8">
<title>Lanternfield Prose Studio</title>
<link href="https://fonts.googleapis.com/css2?family=Kanit:wght@400;500;600&family=Roboto:wght@400;500;700&display=swap" rel="stylesheet">
<style>
:root{
  --orange:#ff5a00;
  --orange-soft:#ff7a2e;
  --cyan:#16c0f0;
  --cyan-text:#1aa9e0;
  --ink:#222222;
  --body:#444444;
  --white:#ffffff;
  --line:#e6e6e6;
}
*{margin:0;padding:0;box-sizing:border-box}
html,body{width:1200px;height:3291px;overflow:hidden;background:var(--white)}
body{position:relative;font-family:'Roboto',sans-serif;color:var(--body)}
.abs{position:absolute}
.heading{font-family:'Kanit',sans-serif;font-weight:500;color:var(--ink);text-transform:uppercase}
.center{text-align:center;left:0;width:1200px}
.rule{position:absolute;height:4px;width:56px;background:var(--ink)}
.btn{position:absolute;display:flex;align-items:center;justify-content:center;border-radius:30px;background:var(--cyan);color:var(--white);font-family:'Roboto',sans-serif;font-weight:500;font-size:15px;text-transform:uppercase}

/* hero */
.hero{left:0;top:0;width:1200px;height:686px;background:linear-gradient(100deg,#7d6f68 0%,#a89a91 35%,#5c6d7c 62%,#3e5468 80%,#6b6f5a 100%)}
.hero-shade{left:0;top:0;width:1200px;height:686px;background:linear-gradient(90deg,rgba(30,30,40,.35) 0%,rgba(30,30,40,.05) 60%)}
.brand-name{font-family:'Kanit',sans-serif;font-weight:500;color:var(--white);line-height:1;letter-spacing:.5px}
.brand-tag{font-family:'Roboto',sans-serif;font-weight:500;color:var(--white);letter-spacing:3px}
.nav{left:460px;top:34px;display:flex;gap:27px;font-size:14px;font-weight:500;color:var(--white);text-transform:uppercase}
.hero-title{left:110px;top:230px;font-family:'Kanit',sans-serif;font-weight:500;font-size:38px;line-height:50px;color:var(--white);text-transform:uppercase}

/* capabilities */
.cap-card{position:absolute;top:895px;width:236px;height:409px;text-align:center}
.cap-card.featured{background:var(--white);box-shadow:0 0 8px rgba(22,192,240,.45);border-radius:3px}
.cap-icon{position:absolute;left:78px;top:38px;width:80px;height:80px}
.cap-title{position:absolute;top:142px;left:0;width:100%;font-family:'Kanit',sans-serif;font-weight:500;font-size:20px;color:var(--cyan-text)}
.cap-text{position:absolute;top:188px;left:18px;width:200px;font-size:15.5px;line-height:24px;color:var(--body)}
.cap-link{position:absolute;top:356px;left:0;width:100%;font-size:15px;font-weight:500;color:var(--cyan-text);text-transform:uppercase}

/* clients */
.clients{left:0;top:1503px;width:1200px;height:449px;background:var(--orange)}
.client-box{position:absolute;top:1721px;width:212px;height:121px;background:var(--white);display:flex;align-items:center;justify-content:center;gap:10px;font-family:'Roboto',sans-serif;font-weight:500;font-size:20px;color:#333333}
.client-dot{width:14px;height:14px;border-radius:50%;background:#333333}

/* work */
.work-card{position:absolute;top:2134px;width:305px;height:382px}
.work-photo{position:absolute;inset:0}
.work-label{position:absolute;left:0;width:100%;text-align:center;font-family:'Kanit',sans-serif;font-weight:500;font-size:24px;color:var(--white);text-transform:uppercase}

/* contact + newsletter */
.contact-panel{left:0;top:2691px;width:600px;height:339px;background:linear-gradient(120deg,#14c3f3 0%,#19b6e8 55%,#2ab8e6 100%)}
.email-field{left:653px;top:2882px;width:424px;height:48px;border:1px solid #999999;border-radius:24px;padding-left:22px;display:flex;align-items:center;font-size:15px;color:#777777}

/* footer */
.footer{left:0;top:3030px;width:1200px;height:261px;background:var(--orange)}
.foot-item{position:absolute;top:3117px;display:flex;align-items:center;gap:12px;color:var(--white);font-size:19px}
.social{position:absolute;top:3213px;width:30px;height:30px;border-radius:50%;background:var(--white)}
</style>
</head>
<body>

<!-- HERO -->
<div class="abs hero" role="img" aria-label="Photo of a businessman in glasses and a blue suit writing at a desk beside a laptop in a bright office"></div>
<div class="abs hero-shade"></div>
<div class="abs" style="left:110px;top:16px">
  <div class="brand-name" style="font-size:29px">LANTERNFIELD</div>
  <div class="brand-tag" style="font-size:12px;margin-top:6px">PROSE STUDIO</div>
</div>
<nav class="abs nav">
  <span>Home</span><span>Our Work</span><span>Capabilities</span><span>About Us</span><span>Blog</span>
</nav>
<div class="btn" style="left:925px;top:25px;width:170px;height:35px">Get in touch</div>
<h1 class="abs hero-title">Communicate your<br>expertise and your<br>coustomer successes</h1>
<div class="btn" style="left:110px;top:409px;width:151px;height:37px">Read more</div>
<svg class="abs" style="left:583px;top:598px" width="30" height="66" viewBox="0 0 30 66" fill="none" stroke="#ffffff" stroke-width="2">
  <rect x="4" y="1" width="22" height="33" rx="11"/>
  <line x1="15" y1="8" x2="15" y2="15"/>
  <polyline points="7,50 15,57 23,50"/>
</svg>

<!-- CAPABILITIES -->
<h2 class="abs heading center" style="top:766px;font-size:28px">Capabilities</h2>
<div class="rule" style="left:572px;top:809px"></div>
<p class="abs center" style="top:838px;font-size:15px;color:#333333">Duis aute irure dolor in reprehenderit in voluptate velit esse cillum dolore eu fugiat nulla pariatur.</p>

<div class="cap-card" style="left:102px">
  <svg class="cap-icon" viewBox="0 0 80 80" fill="none" stroke="#ff5a00" stroke-width="3" stroke-linejoin="round">
    <path d="M40 10a20 20 0 0 0-12 36v10h24V46a20 20 0 0 0-12-36z"/>
    <line x1="30" y1="63" x2="50" y2="63"/><line x1="33" y1="70" x2="47" y2="70"/>
    <circle cx="40" cy="30" r="7"/>
    <line x1="12" y1="30" x2="4" y2="30"/><line x1="68" y1="30" x2="76" y2="30"/>
    <line x1="18" y1="10" x2="12" y2="4"/><line x1="62" y1="10" x2="68" y2="4"/>
  </svg>
  <div class="cap-title">Strategy</div>
  <p class="cap-text">Lorem ipsum dolor sit amet, consectetur adipi scing elit, sed do eiusmod tempor incididunt ut labore et dolore magna aliqua. Ut enim ad minim veniam</p>
  <div class="cap-link">Learn more</div>
</div>

<div class="cap-card featured" style="left:359px">
  <svg class="cap-icon" viewBox="0 0 80 80" fill="none" stroke="#ff5a00" stroke-width="3" stroke-linejoin="round">
    <rect x="10" y="22" width="60" height="40" rx="2"/>
    <path d="M4 66h72v5H4z"/>
    <rect x="26" y="6" width="34" height="22" rx="2" fill="#ffffff"/>
    <line x1="32" y1="13" x2="54" y2="13"/><line x1="32" y1="20" x2="48" y2="20"/>
    <circle cx="28" cy="44" r="5"/><path d="M20 58c0-6 16-6 16 0"/>
    <circle cx="52" cy="44" r="5"/><path d="M44 58c0-6 16-6 16 0"/>
  </svg>
  <div class="cap-title">Coaching</div>
  <p class="cap-text">Lorem ipsum dolor sit amet, consectetur adipi scing elit, sed do eiusmod tempor incididunt ut labore et dolore magna aliqua. Ut enim ad minim veniam</p>
  <div class="cap-link">Learn more</div>
</div>

<div class="cap-card" style="left:612px">
  <svg class="cap-icon" viewBox="0 0 80 80" fill="none" stroke="#ff5a00" stroke-width="3" stroke-linejoin="round">
    <path d="M52 50v24H12V6h40v14"/>
    <line x1="20" y1="18" x2="44" y2="18"/><line x1="20" y1="28" x2="44" y2="28"/>
    <line x1="20" y1="38" x2="38" y2="38"/><line x1="20" y1="48" x2="34" y2="48"/>
    <path d="M66 22l8 8-26 26-11 3 3-11z"/>
  </svg>
  <div class="cap-title">Writing</div>
  <p class="cap-text">Lorem ipsum dolor sit amet, consectetur adipi scing elit, sed do eiusmod tempor incididunt ut labore et dolore magna aliqua. Ut enim ad minim veniam</p>
  <div class="cap-link">Learn more</div>
</div>

<div class="cap-card" style="left:866px">
  <svg class="cap-icon" viewBox="0 0 80 80" fill="none" stroke="#ff5a00" stroke-width="3.5" stroke-linejoin="round">
    <path d="M40 14H12v58h58V44"/>
    <path d="M62 6l10 10-32 32-13 3 3-13z"/>
    <line x1="56" y1="12" x2="66" y2="22"/>
  </svg>
  <div class="cap-title">Editing</div>
  <p class="cap-text">Lorem ipsum dolor sit amet, consectetur adipi scing elit, sed do eiusmod tempor incididunt ut labore et dolore magna aliqua. Ut enim ad minim veniam</p>
  <div class="cap-link">Learn more</div>
</div>

<div class="btn" style="left:482px;top:1356px;width:241px;height:46px">View our capabilities</div>

<!-- CLIENTS -->
<div class="abs clients"></div>
<h2 class="abs heading center" style="top:1556px;font-size:28px;color:var(--white)">Our Clients</h2>
<div class="rule" style="left:572px;top:1603px;background:var(--white)"></div>
<p class="abs center" style="top:1641px;font-size:15px;line-height:26px;color:var(--white)">commodo consequat. Duis aute irure dolor in reprehenderit in voluptate velit esse cillum dolore eu fugiat nulla pariatur.<br>Excepteur sint occaecat cupidatat non proident, sunt in culpa qui</p>
<div class="client-box" style="left:35px"><span class="client-dot"></span>Versewell</div>
<div class="client-box" style="left:262px">Northpage</div>
<div class="client-box" style="left:489px">Inkhaven</div>
<div class="client-box" style="left:717px">Quillmark</div>
<div class="client-box" style="left:944px">Sealbright</div>
<svg class="abs" style="left:558px;top:1876px" width="82" height="24" viewBox="0 0 82 24" fill="none" stroke="#ffffff" stroke-width="2.5">
  <line x1="3" y1="12" x2="35" y2="12"/><polyline points="12,4 3,12 12,20"/>
  <line x1="47" y1="12" x2="79" y2="12"/><polyline points="70,4 79,12 70,20"/>
</svg>

<!-- OUR WORK -->
<h2 class="abs heading" style="left:110px;top:2036px;font-size:28px">Our Work</h2>
<div class="rule" style="left:115px;top:2084px"></div>
<p class="abs" style="left:305px;top:2040px;width:800px;font-size:15px;line-height:26px;color:#333333">sunt in culpa qui officia deserunt mollit anim id est laborumSed ut perspiciatis unde omnis iste natus error sit voluptatem accusantium doloremque laudantium, totam rem aperiam, eaque ipsa quae ab illo inventore veritatis</p>

<div class="work-card" style="left:111px">
  <div class="work-photo" role="img" aria-label="Photo of a young woman in a grey sweater writing in a notebook at a white desk" style="background:linear-gradient(160deg,#f1efed 0%,#d9d6d4 45%,#8d8f94 100%)"></div>
  <div class="work-label" style="top:2466px;top:332px">Voluptatem</div>
</div>

<div class="work-card" style="left:451px">
  <div class="work-photo" role="img" aria-label="Photo of a woman at a desk beneath an orange colour overlay" style="background:linear-gradient(160deg,#ff7d2a 0%,#ff6a12 55%,#f46210 100%)"></div>
  <div class="work-label" style="top:86px;font-size:20px;line-height:26px;padding:0 30px">How to align your applications to theoptimal</div>
  <p class="abs" style="left:0;top:194px;width:100%;text-align:center;font-size:15px;line-height:26px;color:var(--white)">Avoiding the Pressure to mOve every<br>Workload to the Public Cloud</p>
  <div class="abs" style="left:0;top:266px;width:100%;display:flex;justify-content:center;align-items:center;gap:8px;font-size:15px;font-weight:500;color:var(--white)">READ MORE
    <svg width="20" height="16" viewBox="0 0 20 16" fill="none" stroke="#ffffff" stroke-width="2.5"><line x1="1" y1="8" x2="18" y2="8"/><polyline points="11,1 18,8 11,15"/></svg>
  </div>
</div>

<div class="work-card" style="left:790px">
  <div class="work-photo" role="img" aria-label="Photo of a smiling woman with curly hair talking on the phone while taking notes" style="background:linear-gradient(160deg,#eef0f2 0%,#cdd4dc 45%,#7d8b99 100%)"></div>
  <div class="work-label" style="top:330px">Reprehenderit</div>
</div>

<div class="btn" style="left:496px;top:2557px;width:207px;height:46px">View our work</div>

<!-- CONTACT -->
<div class="abs contact-panel" role="img" aria-label="Faded photo of a hand writing with a pen under a bright cyan overlay"></div>
<h2 class="abs heading" style="left:0;width:600px;text-align:center;top:2754px;font-size:28px;color:var(--white)">Contact us</h2>
<div class="rule" style="left:270px;top:2803px;background:var(--white)"></div>
<p class="abs" style="left:0;width:600px;text-align:center;top:2828px;font-family:'Kanit',sans-serif;font-weight:500;font-size:20px;line-height:34px;color:var(--white);text-transform:uppercase">Feel free to contact us with<br>any questions. We're happy to help</p>
<div class="btn" style="left:201px;top:2915px;width:191px;height:43px;background:var(--orange)">Get in touch</div>

<h2 class="abs heading" style="left:657px;top:2722px;font-size:28px">Newsletter</h2>
<div class="rule" style="left:658px;top:2771px"></div>
<p class="abs" style="left:658px;top:2800px;font-family:'Kanit',sans-serif;font-weight:500;font-size:19px;line-height:30px;color:var(--ink);text-transform:uppercase">Editorial inspiration delivered<br>straight to your inbox</p>
<div class="abs email-field">Email Address</div>
<div class="btn" style="left:657px;top:2945px;width:129px;height:44px">Submit</div>

<!-- FOOTER -->
<div class="abs footer"></div>
<div class="abs" style="left:110px;top:3082px">
  <div class="brand-name" style="font-size:34px">LANTERNFIELD</div>
  <div class="brand-tag" style="font-size:14px;margin-top:8px;letter-spacing:4px">PROSE STUDIO</div>
</div>
<div class="abs" style="left:110px;top:3172px;font-size:17px;font-weight:500;color:var(--white)">FOLLOW US</div>
<div class="social" style="left:110px" aria-label="Social link"></div>
<div class="social" style="left:146px" aria-label="Social link"></div>
<div class="social" style="left:183px" aria-label="Social link"></div>
<div class="social" style="left:220px" aria-label="Social link"></div>

<div class="foot-item" style="left:414px">
  <svg width="16" height="24" viewBox="0 0 16 24" fill="#ffffff"><path d="M8 0a8 8 0 0 0-8 8c0 6 8 16 8 16s8-10 8-16a8 8 0 0 0-8-8zm0 11a3 3 0 1 1 0-6 3 3 0 0 1 0 6z"/></svg>
  <span>123ut aliquid ex ea</span>
</div>
<div class="foot-item" style="left:671px">
  <svg width="24" height="24" viewBox="0 0 24 24" fill="#ffffff"><path d="M5 1l4 1 2 6-3 2a14 14 0 0 0 6 6l2-3 6 2 1 4-3 4C10 23 1 14 1 4z"/></svg>
  <span>(555)-014-2298</span>
</div>
<div class="foot-item" style="left:925px">
  <svg width="28" height="20" viewBox="0 0 28 20" fill="none" stroke="#ffffff" stroke-width="2"><rect x="1" y="1" width="26" height="18"/><polyline points="1,1 14,11 27,1"/><line x1="1" y1="19" x2="11" y2="9"/><line x1="27" y1="19" x2="17" y2="9"/></svg>
  <span>hello@lpstudio.net</span>
</div>
<div class="abs" style="left:419px;top:3180px;width:676px;height:1px;background:rgba(255,255,255,.6)"></div>
<p class="abs" style="left:419px;top:3219px;width:676px;text-align:right;font-size:15px;color:var(--white)">Copyright 2021 Lanternfield Prose Studio, All Rights Reserved</p>

</body>
</html>
```